BrindleFlow Van Wrap Design

We are home heating specialists. We fit boilers and central heating systems as well as servicing and repairing boilers in domestic properties. We have a new logo and need our vans design to undergo some modernisation. Our vans are Short wheel base carrow plus.
Website www.BrindleFlow.co.uk
Phone 01632 958274
List of work we do:
Central heating
Installation,
Servicing,
Repairs,
Target Market(s)
Home owners and landlords
Industry/Entity Type
Gas, central heating
Font styles to use
Other font styles liked:
- See logo fonts
Colors
0054AA
0677BA
7BADD7
CADEEF
E8F1F8
EE7325
F08F49
F5BC92
FAE3D3
FDF4ED
Requirements
Must have
- Phone number, logo, web address, Chatterly logo, fuel sound logo, Halden Kruse logo, list of work we do
Nice to have
- Warm design as we are heating specialists.
Should not have
- Too much blue. Our main colour is orange.

```html
<!DOCTYPE html>
<html lang="en">
<head>
<meta charset="utf-8">
<title>BrindleFlow Van Wrap</title>
<link rel="stylesheet" href="https://fonts.googleapis.com/css2?family=Montserrat:wght@500;600;700;800&display=swap">
<style>
  :root {
    --blue-deep: #0054AA;
    --blue: #2b6cc4;
    --orange: #EE7325;
    --orange-soft: #F08F49;
    --orange-pale: #F5BC92;
    --orange-mist: #FAE3D3;
    --panel: #ececec;
    --panel-edge: #dcdcdc;
    --bg: #d4d4d4;
    --badge: #cfcfcf;
  }
  * { margin: 0; padding: 0; box-sizing: border-box; }
  html, body { width: 1200px; height: 1000px; overflow: hidden; }
  body {
    background: linear-gradient(180deg, #f4f4f4 0%, var(--bg) 60%, #bdbdbd 100%);
    font-family: "Montserrat", sans-serif;
    position: relative;
  }
  .wrap-panel {
    position: absolute;
    left: 80px; top: 250px;
    width: 1050px; height: 400px;
    border-radius: 60px 40px 20px 20px;
    background: var(--panel);
    overflow: hidden;
    box-shadow: inset 0 0 0 2px var(--panel-edge);
  }
  .halftone-front {
    position: absolute; left: 0; top: 120px; width: 360px; height: 280px;
    background: radial-gradient(ellipse at 20% 80%, var(--orange-soft) 0%, var(--orange-pale) 45%, rgba(245,188,146,0) 75%);
  }
  .halftone-rear {
    position: absolute; right: 0; top: 0; width: 300px; height: 400px;
    background: linear-gradient(200deg, rgba(245,188,146,0) 0%, var(--orange-pale) 45%, var(--orange-soft) 100%);
  }
  .rear-band {
    position: absolute; right: 0; bottom: 0; width: 200px; height: 120px;
    background: linear-gradient(180deg, var(--orange-soft), var(--orange));
  }
  .accreditations {
    position: absolute; left: 362px; top: 503px;
    display: flex; align-items: center; gap: 14px;
  }
  .badge-fuel-sound {
    width: 56px; height: 58px; background: var(--badge);
  }
  .partner-name {
    font-weight: 700; font-size: 15px; color: var(--blue-deep);
    letter-spacing: 0.2px; white-space: nowrap;
  }
  .brand-block {
    position: absolute; left: 594px; top: 285px; width: 320px;
  }
  .brand-mark {
    display: block; width: 90px; height: 90px; border-radius: 50%;
    background: var(--orange); margin: 0 0 12px 88px;
  }
  .brand-name {
    font-size: 49px; font-weight: 600; color: var(--orange);
    line-height: 1; letter-spacing: -0.5px;
  }
  .tagline {
    font-size: 10.5px; font-weight: 600; color: var(--blue);
    letter-spacing: 3.9px; margin-top: 4px; white-space: nowrap;
  }
  .web { font-size: 20.5px; font-weight: 600; color: var(--blue); margin-top: 8px; white-space: nowrap; }
  .social {
    display: flex; justify-content: flex-end; align-items: center; gap: 5px;
    width: 252px; font-size: 19px; font-weight: 600; color: var(--blue); margin-top: 1px;
  }
  .social-dot { width: 12px; height: 12px; border-radius: 50%; background: var(--blue); }
  .phone { font-size: 33px; font-weight: 800; color: var(--blue-deep); margin-top: 6px; letter-spacing: 0.3px; white-space: nowrap; }
  .services { font-size: 14.3px; font-weight: 700; color: var(--blue); line-height: 17px; margin-top: 4px; white-space: nowrap; }
  .services .sep { color: var(--orange); }
</style>
</head>
<body>
  <section class="wrap-panel" aria-label="Van side wrap">
    <div class="halftone-front" role="img" aria-label="Orange halftone dot pattern fading across the front"></div>
    <div class="halftone-rear" role="img" aria-label="Orange halftone dot pattern across the rear"></div>
    <div class="rear-band"></div>
  </section>

  <div class="accreditations">
    <div class="badge-fuel-sound" role="img" aria-label="fuel sound registration badge"></div>
    <span class="partner-name">Halden Kruse</span>
  </div>

  <div class="brand-block">
    <span class="brand-mark"></span>
    <div class="brand-name">BrindleFlow</div>
    <div class="tagline">YOUR HOME HEATING SPECIALISTS</div>
    <div class="web">www.BrindleFlow.co.uk</div>
    <div class="social"><span class="social-dot"></span>BrindleFlow</div>
    <div class="phone">01632 958274</div>
    <div class="services">
      Installation <span class="sep">•</span> Servicing <span class="sep">•</span> Repairs<br>
      <span class="sep">+</span> Boilers <span class="sep">+</span> Fire Places<br>
      <span class="sep">+</span> Gas Appliances
    </div>
  </div>
</body>
</html>
```